Business card design needed

It's a new business in town.Something so the name stands out.I need a logo for the B.R.W
I may all so use the design as a sign on a building

Contact Information for Business Card

B.R.W
Brindlewood Auto Detailing
42 Fenwarra Crs
Brindlewood Vic 3799
Ph:(03)59284736
Mob:0417362958

```html
<!DOCTYPE html>
<html lang="en">
<head>
<meta charset="utf-8">
<title>Brindlewood Auto Detailing – Business Card</title>
<link rel="stylesheet" href="https://fonts.googleapis.com/css2?family=Didact+Gothic&display=swap">
<style>
  :root {
    --paper: #ffffff;
    --ink: #111111;
    --disc-light: #ebebeb;
    --ring-mid: #d4d4d4;
    --gear-edge: #b3b3b3;
    --gear-centre: #dedede;
    --nut-tone: #c2c2c2;
    --rule: #b5b5b5;
  }
  html, body {
    margin: 0;
    padding: 0;
    overflow: hidden;
    background: var(--paper);
  }
  .card {
    position: relative;
    width: 1200px;
    height: 741px;
    overflow: hidden;
    background: var(--paper);
    font-family: "Didact Gothic", sans-serif;
    color: var(--ink);
  }
  .backdrop, .machine-art {
    position: absolute;
    inset: 0;
  }
  .brand-name {
    position: absolute;
    left: 44px;
    top: 118px;
    margin: 0;
    font-size: 246px;
    line-height: 1;
    font-weight: 400;
    letter-spacing: 28px;
    color: var(--ink);
  }
  .business-name {
    position: absolute;
    left: 50px;
    top: 372px;
    margin: 0;
    font-size: 57px;
    font-weight: 400;
    line-height: 1;
    letter-spacing: 0.5px;
  }
  .address {
    position: absolute;
    left: 52px;
    top: 452px;
    margin: 0;
    font-size: 38px;
    line-height: 1;
    letter-spacing: 0.5px;
  }
  .contact {
    position: absolute;
    left: 50px;
    top: 593px;
    margin: 0;
    font-size: 43px;
    line-height: 59px;
  }
  .contact span { display: block; }
</style>
</head>
<body>
  <main class="card">
    <svg class="backdrop" width="1200" height="741" viewBox="0 0 1200 741" aria-hidden="true">
      <circle class="left-ring" cx="314" cy="227" r="322" fill="none" stroke="var(--ring-mid)" stroke-width="28"/>
      <circle class="left-disc" cx="314" cy="227" r="308" fill="var(--disc-light)"/>
      <line class="divider" x1="49" y1="362" x2="770" y2="362" stroke="var(--rule)" stroke-width="4"/>
    </svg>

    <svg class="machine-art" width="1200" height="741" viewBox="0 0 1200 741"
         role="img" aria-label="Grey gear wheel and hex nut illustration">
      <defs>
        <radialGradient id="gear-tone" cx="0.5" cy="0.5" r="0.5">
          <stop offset="0.75" stop-color="var(--gear-centre)"/>
          <stop offset="1" stop-color="var(--gear-edge)"/>
        </radialGradient>
      </defs>
      <circle class="gear-area" cx="1081" cy="627" r="331" fill="url(#gear-tone)"/>
      <circle class="nut-area" cx="827" cy="355" r="60" fill="var(--nut-tone)"/>
    </svg>

    <h1 class="brand-name">B.R.W</h1>
    <p class="business-name">Brindlewood Auto Detailing</p>
    <p class="address">42 Fenwarra Crs Brindlewood Vic 3799</p>
    <p class="contact">
      <span class="phone">Ph:(03)59284736</span>
      <span class="mobile">Mob:0417362958</span>
    </p>
  </main>
</body>
</html>
```